A new company focused on starting and investing in transformative businesses.

We need a simple and clean website with a few pages. we like larkmeadow.com as a starting point. we want the landing page to be very simple with an option to click through on the top right into INVESTOR LOGIN. then we want to be able to scroll down to see more about our company.

Target Market(s)

professional

Coding

Coded - Design and coding required

Number of Pages Required

2 page

Font styles to use
Serif
Sans Serif

Requirements
Must have
• HALVERN BUILDERS logo (attached as a file) on the top with INVESTOR LOGIN as a click through on the right. Please model the click through from larkmeadow.com. The description (also written in attached file) should be on the landing page. we do not want to have to scroll to read the description.

Then we can scroll down to read more about Halvern including the mission and the two types of businesses. More is detailed on the attached file called "Halvern Website Syntax"
Should not have
• should not be slow loading with lots of fancy graphics. should not be busy and with too many colors.

```html
<!DOCTYPE html>
<html lang="en">
<head>
<meta charset="utf-8">
<title>Halvern Builders</title>
<link href="https://fonts.googleapis.com/css2?family=Lato:wght@400;700&display=swap" rel="stylesheet">
<style>
  :root {
    --brand-blue: #0b4596;
    --mission-blue: #0d3f85;
    --ink: #1c1c1c;
    --white: #ffffff;
    --footer-grey: #f1f1f1;
  }
  * { box-sizing: border-box; margin: 0; padding: 0; }
  html, body { width: 973px; height: 1200px; overflow: hidden; }
  body { font-family: 'Lato', sans-serif; color: var(--ink); background: var(--white); position: relative; }

  .hero { position: absolute; left: 0; top: 0; width: 973px; height: 599px; }
  .hero-backdrop {
    position: absolute; inset: 0;
    background:
      radial-gradient(ellipse 360px 300px at 700px 330px, #e6e6e6 0%, #bdbdbd 45%, rgba(120,120,120,0) 100%),
      linear-gradient(100deg, #4a4a4a 0%, #6b6b6b 40%, #9a9a9a 70%, #8a8a8a 100%);
  }
  .brand { position: absolute; left: 61px; top: 40px; display: flex; align-items: center; gap: 12px; }
  .brand-mark { width: 40px; height: 48px; background: var(--brand-blue); }
  .brand-name { font-weight: 700; font-size: 24px; line-height: 26px; color: var(--white); letter-spacing: 1px; width: 150px; }
  .investor-login {
    position: absolute; left: 762px; top: 46px; width: 151px; height: 38px;
    border: 2px solid var(--white); color: var(--white); text-decoration: none;
    font-weight: 700; font-size: 12px; letter-spacing: 0.3px;
    display: flex; align-items: center; justify-content: center;
  }
  .hero-title {
    position: absolute; left: 61px; top: 195px; width: 500px;
    font-weight: 400; font-size: 36px; line-height: 50px; color: var(--white);
  }
  .scroll-arrow { position: absolute; left: 62px; top: 508px; }

  .about { position: absolute; left: 0; top: 599px; width: 973px; height: 346px; }
  .mission {
    position: absolute; left: 61px; top: 47px; width: 420px;
    font-weight: 400; font-size: 25px; line-height: 42px; color: var(--mission-blue);
  }
  .ventures { position: absolute; left: 499px; top: 50px; width: 420px; }
  .venture-title { font-weight: 700; font-size: 25px; line-height: 32px; margin-bottom: 8px; }
  .venture-text { font-size: 13px; line-height: 24px; margin-bottom: 22px; }

  .contact { position: absolute; left: 0; top: 945px; width: 973px; height: 175px; background: var(--footer-grey); }
  .contact-name { position: absolute; left: 61px; top: 55px; font-weight: 700; font-size: 25px; }
  .contact-text { position: absolute; left: 61px; top: 105px; font-size: 13px; }
  .contact-text a { color: var(--brand-blue); text-decoration: none; }
  .contact-brand { position: absolute; left: 587px; top: 35px; display: flex; align-items: center; gap: 20px; }
  .contact-brand .brand-mark { width: 88px; height: 108px; }
  .contact-brand-name { font-weight: 700; font-size: 42px; line-height: 46px; color: var(--ink); letter-spacing: 1px; }

  .legal { position: absolute; left: 0; top: 1120px; width: 973px; height: 80px; }
  .copyright { position: absolute; left: 61px; top: 32px; font-size: 12px; }
  .social { position: absolute; left: 727px; top: 32px; display: flex; gap: 23px; list-style: none; }
  .social li { width: 19px; height: 19px; border-radius: 50%; background: var(--ink); }
</style>
</head>
<body>
  <header class="hero">
    <div class="hero-backdrop" role="img" aria-label="Grey textured backdrop with two groups of chess pawns casting a shared shadow shaped like a crown"></div>
    <div class="brand">
      <span class="brand-mark"></span>
      <span class="brand-name">HALVERN BUILDERS</span>
    </div>
    <a class="investor-login" href="#">INVESTOR LOGIN</a>
    <h1 class="hero-title">Halvern Builders is an entrepreneurial firm focused on building and growing transformational companies</h1>
    <svg class="scroll-arrow" width="18" height="34" viewBox="0 0 18 34" aria-hidden="true">
      <rect x="6.5" y="0" width="5" height="24" fill="#0b4596"/>
      <polygon points="0,20 18,20 9,34" fill="#0b4596"/>
    </svg>
  </header>

  <section class="about">
    <p class="mission">Our mission is into build meaningful businesses that create enduring value by impacting people in a measurable way.</p>
    <div class="ventures">
      <h2 class="venture-title">Ground Up</h2>
      <p class="venture-text">Our ground up business applies a proven analytic process to identify value edge, a form of competitive advantage. We architect transformational&nbsp; companies and are deliberate in creating the foundation necessary to lead an industry.</p>
      <h2 class="venture-title">Special Opportunities</h2>
      <p class="venture-text">We partner with exceptional teams that create value by transforming lives.</p>
    </div>
  </section>

  <section class="contact">
    <h2 class="contact-name">Halvern Builders</h2>
    <p class="contact-text">For media inquiries, please contact <a href="mailto:nora@halvernbuilders.com">nora@halvernbuilders.com</a></p>
    <div class="contact-brand">
      <span class="brand-mark"></span>
      <span class="contact-brand-name">HALVERN<br>BUILDERS</span>
    </div>
  </section>

  <footer class="legal">
    <p class="copyright">Copyright © 2021, Company Name. All Right reserved</p>
    <ul class="social" aria-label="Social links">
      <li></li><li></li><li></li><li></li><li></li>
    </ul>
  </footer>
</body>
</html>
```